Buchcover-Design für Fragenbuch
Ganz herzlichen Dank. Die Zusammenarbeit war völlig reibungslos und entspannt. Änderungswünsche wurden professionell umgesetzt und die kreativen Vorschläge fand ich super. Ich bin total glücklich mit dem Ergebnis.
Zielgruppe
Autorin und Workshopleiterin. Zielgruppe: Frauen ab 30
Aufgabenstellung
Ich benötige ein komplettes Buchcover, sowie 12 farbige Innenseiten. Es geht um ein Fragenbuch zum Ausfüllen mit dem Titel:
„Finde zurück zur leisen Mitte
Ein Arbeitsheft zum Eintragen für tiefere seelische Ruhe“
Das Format des Buches beträgt 17x22cm. Es ist in 12 Wochen unterteilt. Darum hätte ich gerne zwischen den einzelnen Wochen eine farbige Seite (1. Woche, 2. Woche etc.), die designmäßig mit dem Außencover korrespondiert.
Die Farben sollten eher zart oder gedeckt sein. Auf keinen Fall jedoch kitschig. Wichtig ist mir, dass keine bestimmte Person zu sehen ist. (Foto)
Das ist meine Website www.finde-zurueck-zur-leisen-mitte.de

```html
<!DOCTYPE html>
<html lang="de">
<head>
<meta charset="utf-8">
<title>Finde zurück zur leisen Mitte – Cover und Innenseiten</title>
<link href="https://fonts.googleapis.com/css2?family=Josefin+Sans:wght@200;300&family=Cormorant+Garamond:wght@600;700&family=Open+Sans:wght@400;700&family=Allura&display=swap" rel="stylesheet">
<style>
  :root {
    --stage: #d9d9d8;
    --ink: #3a2a22;
    --ink-soft: #8a7a6e;
    --paper: #fbfbfa;
    --sand: #e4dcd2;
    --sand-light: #ece6df;
    --taupe: #c6b7a9;
    --taupe-deep: #b9a690;
    --frame: #a99580;
    --sepia-light: #cbb8a6;
    --sepia-dark: #5a4434;
  }
  * { margin: 0; padding: 0; box-sizing: border-box; }
  html, body { width: 1200px; height: 960px; overflow: hidden; }
  body { background: var(--stage); position: relative; font-family: "Open Sans", sans-serif; color: var(--ink); }

  .page { position: absolute; top: 260px; width: 340px; height: 440px; overflow: hidden; box-shadow: 0 6px 18px rgba(0,0,0,.12); }

  /* Week opener page */
  .week-page { left: 40px; background: linear-gradient(90deg, var(--taupe) 0%, #cdbfb2 85%, #d8ccc0 100%); }
  .week-page .photo-frame { position: absolute; left: 150px; top: 0; width: 190px; height: 182px; background: var(--frame); border-radius: 0 0 36px 0; }
  .week-page .photo { position: absolute; left: 162px; top: 0; width: 170px; height: 166px; border-radius: 30px 0 30px 0;
    background: radial-gradient(circle at 40% 45%, #f4efe8 0%, #e0d2c2 45%, #8a6a50 100%); }
  .week-number { position: absolute; left: 26px; top: 40px; font-family: "Josefin Sans", sans-serif; font-weight: 200; font-size: 120px; line-height: 1; }
  .week-label { position: absolute; left: 78px; top: 152px; font-family: "Josefin Sans", sans-serif; font-weight: 300; font-size: 34px; letter-spacing: 1px; }
  .module { position: absolute; left: 110px; top: 262px; width: 200px; text-align: center; }
  .module-kicker { font-family: "Josefin Sans", sans-serif; font-weight: 300; font-size: 11px; letter-spacing: .5px; }
  .module-title { font-family: "Cormorant Garamond", serif; font-weight: 700; font-size: 24px; letter-spacing: 1px; margin-top: 6px; }
  .module-rule { width: 110px; height: 1px; background: rgba(58,42,34,.25); margin: 10px auto 0; }

  /* Content page */
  .content-page { left: 380px; background: linear-gradient(90deg, #ececeb 0%, var(--paper) 12%); }
  .content-page .photo-top { position: absolute; left: 32px; top: 30px; width: 290px; height: 172px;
    background: linear-gradient(135deg, var(--sepia-light), #a58b76 60%, #7e6452); }
  .content-page .photo-side { position: absolute; left: 175px; top: 220px; width: 165px; height: 150px;
    background: linear-gradient(160deg, #7a5d49, var(--sepia-dark) 60%, #3e2d22); }
  .column-text { position: absolute; left: 32px; top: 225px; width: 128px; font-size: 7px; line-height: 1.6; color: #5a4a40; }
  .column-text strong { display: block; margin-top: 12px; color: var(--ink); }
  .column-text .wave { display: block; margin-top: 6px; }
  .zigzag { position: absolute; left: 40px; top: 385px; }

  /* Cover */
  .cover { left: 800px; background: linear-gradient(180deg, var(--sand) 0%, #e6ded5 100%); }
  .cover-frame { position: absolute; left: 55px; top: 68px; width: 262px; height: 262px; background: var(--taupe-deep); border-radius: 80px 8px 70px 8px; }
  .cover-panel { position: absolute; left: 95px; top: 88px; width: 202px; height: 200px; background: var(--sand-light); border-radius: 8px 8px 52px 8px; }
  .portrait { position: absolute; left: 134px; top: 125px; width: 132px; height: 132px; border-radius: 50%;
    background: radial-gradient(circle at 50% 45%, #c9b4a4 0%, #8e8478 55%, #b7b0a4 100%); }
  .cover-title { position: absolute; left: 0; top: 38px; font-family: "Josefin Sans", sans-serif; font-weight: 300; font-size: 34px; line-height: .92; text-transform: uppercase; }
  .cover-title span { display: block; }
  .cover-title .l1 { margin-left: 70px; }
  .cover-title .l2 { margin-left: 86px; }
  .cover-title .l3 { margin-left: 52px; }
  .cover-title .l4 { margin-left: 70px; }
  .cover-subtitle { position: absolute; left: 62px; top: 318px; width: 260px; }
  .cover-subtitle .kind { font-family: "Cormorant Garamond", serif; font-weight: 700; font-size: 23px; letter-spacing: 1px; text-transform: uppercase; }
  .cover-subtitle .line { font-size: 9.5px; color: #5a4a40; margin-top: 1px; }
  .author { position: absolute; left: 0; width: 340px; top: 372px; text-align: center; font-family: "Allura", cursive; font-size: 26px; color: var(--ink-soft); }
</style>
</head>
<body>

  <section class="page week-page">
    <div class="photo-frame"></div>
    <div class="photo" role="img" aria-label="Foto: halbierte Kokosnüsse in warmen Beigetönen"></div>
    <div class="week-number">2</div>
    <div class="week-label">WOCHE</div>
    <div class="module">
      <div class="module-kicker">TITLE OR HEADLINE HERE</div>
      <div class="module-title">YOUR MODULE</div>
      <div class="module-rule"></div>
    </div>
  </section>

  <section class="page content-page">
    <div class="photo-top" role="img" aria-label="Foto: Blätter und Rosen in Sepiatönen"></div>
    <div class="photo-side" role="img" aria-label="Foto: dunkler Innenraum mit Wandleuchten in Sepiatönen"></div>
    <div class="column-text">
      Nimm dir jeden Morgen einen Moment nur für dich. Atme tief ein, spüre nach und schreibe auf, was dich gerade bewegt. Es gibt kein Richtig oder Falsch, nur deine ehrliche Antwort auf diese Frage.
      <svg class="wave" width="40" height="6" viewBox="0 0 40 6"><polyline points="0,3 4,1 8,5 12,1 16,5 20,1 24,5 28,1 32,5 36,1 40,3" fill="none" stroke="#7a6a60" stroke-width=".8"/></svg>
      <strong>Was brauchst du heute wirklich?</strong>
    </div>
    <svg class="zigzag" width="300" height="10" viewBox="0 0 300 10">
      <polyline fill="none" stroke="#8a8a88" stroke-width=".8"
        points="0,5 4,2 8,8 12,2 16,8 20,2 24,8 28,2 32,8 36,2 40,8 44,2 48,8 52,2 56,8 60,2 64,8 68,2 72,8 76,2 80,8 84,2 88,8 92,2 96,8 100,2 104,8 108,2 112,8 116,2 120,8 124,2 128,8 132,2 136,8 140,2 144,8 148,2 152,8 156,2 160,8 164,2 168,8 172,2 176,8 180,2 184,8 188,2 192,8 196,2 200,8 204,2 208,8 212,2 216,8 220,2 224,8 228,2 232,8 236,2 240,8 244,2 248,8 252,2 256,8 260,2 264,8 268,2 272,8 276,2 280,8 284,2 288,8 292,2 296,8 300,5"/>
    </svg>
  </section>

  <section class="page cover">
    <div class="cover-frame"></div>
    <div class="cover-panel"></div>
    <div class="portrait" role="img" aria-label="Porträtfoto im Kreis"></div>
    <h1 class="cover-title">
      <span class="l1">Finde</span>
      <span class="l2">zurück</span>
      <span class="l3">zur leisen</span>
      <span class="l4">Mitte</span>
    </h1>
    <div class="cover-subtitle">
      <div class="kind">Ein Arbeitsheft</div>
      <div class="line">zum Eintragen für tiefere seelische Ruhe</div>
    </div>
    <div class="author">by Lena Morwitz</div>
  </section>

</body>
</html>
```